Help make our corporate website modern and cool with graphical elements and icons

We are makers of cloud infrastructure software (www.nimbrotek.com) and our target audience is developers. Developers generally want text and icons, they don't care for photos. They want good usability and easy-to-find information. Think forkhive.com, cloud.zephyrqa.com, www.stackmoor.com, pallork.com for reference.

Your challenge will be to modernize the site and make it look "cool" from a developer's point-of-view while still keeping the basic site structure. You can add graphical elements that make the pages come more alive, suggest different layout options, and incorporate icons that we've recently developed (I've attached them for your review). We will keep the Nimbrotek blue and gray, but you are free to add complementary colors in your designs to help spice up the page. See the complementary colors we've used in the icons package.

A successful design will keep the core identity of our website but will make the pages more exciting and compelling to visit, and make the visitor want to scroll and click to dive in deeper into the site. I also want to see additional mock-ups for the main landing pages (Why Nimbrotek, Products, Community, and a new landing page for Resources).

We use WordPress and the Q theme, so if you have familiarity with that theme and its capabilities, even better.

Target Market(s)

Mobile and Web application developers from larger organizations. Developers typically don't like stock images of people or landscapes, they usually just want the information they're looking for presented in a clean and organized way. That said, they do like it if an icon or design element helps them visualize the information. So the design should be useful and necessary to the info provided.

Industry/Entity Type

Computer Software

Number of Pages Required

5+ page

Font styles to use
Sans Serif
Other font styles liked:
• We use Lato as our main font

Colors

Designer to choose colors to be used in the design.

Requirements
Must have
• Must haves:
• - clean and modern design, not too busy but still visually engaging
• - keep the core identity of the site while adding graphical elements/icons
• - use either the hexagons from the icons or incorporate the venn diagram shape somehow from https://www.nimbrotek.com/why-nimbrotek/
• - shapes and icons are preferred over photos or stock "tech" images
• - should keep the nimbrotek blue and gray but can have complementary accent colors (see the icon colors that I've attached)
• - you can use the attached icons
• - make the information appealing to view, scroll and click through
• - design must not interfere with navigation or readability, must complement and be appropriate for the specific information shown
• - use pallork.com and cloud.zephyrqa.com for reference
Nice to have
• nice to haves:
• - familiarity with Zephyrqa Run Engine and cloud computing
• - easy to implement on WordPress, familiarity with Q theme a plus
• - ability to identify with app developers
Should not have
• - unfortunately, stock photos of people or landscapes won't work
• - don't use clip art of clouds or other stock images of high tech
• - don't make it too busy, we are looking for clean and modern

```html
<!DOCTYPE html>
<html lang="en">
<head>
<meta charset="utf-8">
<title>Nimbrotek – Multi cloud native</title>
<link href="https://fonts.googleapis.com/css2?family=Lato:wght@300;400;700&display=swap" rel="stylesheet">
<style>
:root{
  --blue-deep:#1e9fd6;
  --blue-teal:#22d0d8;
  --accent:#f6b42c;
  --ink:#3a3f47;
  --muted:#c9ccd1;
  --paper:#ffffff;
  --gray-band:#f2f3f5;
}
*{box-sizing:border-box;margin:0;padding:0}
html,body{width:1179px;height:1200px;overflow:hidden}
body{font-family:"Lato",sans-serif;color:var(--ink);background:var(--paper);position:relative}

.hero{position:absolute;left:0;top:0;width:1179px;height:676px;
  background:linear-gradient(100deg,var(--blue-deep) 0%,#20bcd8 55%,var(--blue-teal) 100%);overflow:hidden;color:#fff}
.hero-backdrop{position:absolute;inset:0;
  background:radial-gradient(ellipse 520px 380px at 880px 300px,rgba(255,255,255,.08),rgba(255,255,255,0) 70%)}

.site-nav{position:absolute;left:66px;right:74px;top:13px;height:38px;display:flex;align-items:center}
.brand{font-size:27px;font-weight:400;letter-spacing:-.3px;color:#fff}
.nav-links{display:flex;list-style:none;margin-left:auto}
.nav-links li{font-size:13.5px;font-weight:700;margin-right:51px;white-space:nowrap}
.nav-links li.has-menu::after{content:"";display:inline-block;width:5px;height:5px;border-right:1.4px solid #fff;border-bottom:1.4px solid #fff;transform:rotate(45deg);margin-left:6px;position:relative;top:-3px}
.nav-cta{border:1px solid #fff;font-size:12.5px;font-weight:700;padding:10px 15px;white-space:nowrap}

.hero-copy{position:absolute;left:66px;top:146px;width:600px}
.hero-title{font-size:42.5px;font-weight:700;line-height:52px;letter-spacing:-.3px}
.hero-lead{margin-top:24px;font-size:16.5px;font-weight:400;line-height:26px;width:580px}
.hero-actions{margin-top:50px;display:flex;gap:10px}
.btn{display:inline-flex;align-items:center;justify-content:center;height:45px;font-size:13px;font-family:inherit}
.btn-outline{width:140px;border:1px solid #fff;color:#fff}
.btn-accent{width:140px;background:var(--accent);color:#fff}
.btn-accent b{font-weight:700;margin-left:3px}

.platforms{position:absolute;left:0;top:605px;width:1179px;height:71px;background:rgba(18,120,175,.16);
  display:flex;align-items:center;justify-content:space-between;padding:0 62px 0 66px}
.platform{display:flex;align-items:center;gap:6px;font-size:12px;font-weight:700;color:#fff;white-space:nowrap}
.platform .mark{width:10px;height:10px;border:1.5px solid #fff;border-radius:50%}

.feature{position:absolute;left:0;top:761px;width:1179px;height:407px}
.shot{position:absolute;left:0;top:0;width:578px;height:407px;background:#fff;box-shadow:0 6px 30px rgba(0,0,0,.08)}
.shot svg{position:absolute;inset:0}
.shot-label{position:absolute;left:0;right:0;top:195px;text-align:center;font-size:12.5px;color:var(--muted)}

.feature-copy{position:absolute;left:642px;top:50px;width:445px}
.feature-title{margin-top:20px;font-size:21px;font-weight:700;color:var(--ink);letter-spacing:-.1px}
.feature-text{margin-top:20px;font-size:14px;line-height:21.5px;color:var(--ink)}
.feature-copy .btn-accent{margin-top:22px;height:40px;width:140px;font-size:12.5px}

.footer-band{position:absolute;left:0;top:1168px;width:1179px;height:32px;background:var(--gray-band)}
</style>
</head>
<body>

<header class="hero">
  <div class="hero-backdrop" role="img" aria-label="Soft decorative backdrop in the hero blue tones"></div>

  <nav class="site-nav">
    <div class="brand">Nimbrotek</div>
    <ul class="nav-links">
      <li>Why Nimbrotek?</li>
      <li class="has-menu">Products</li>
      <li>Community</li>
      <li class="has-menu">Resources</li>
      <li>Contact Us</li>
    </ul>
    <a class="nav-cta">Try Nimbrotek</a>
  </nav>

  <div class="hero-copy">
    <h1 class="hero-title">Multi cloud native.<br>Serverless by design.<br>NoOps as a first principle.</h1>
    <p class="hero-lead">Nimbrotek is an easy-to-manage serverless platform for building and running scalable web and mobile applications on any infrastructure. Build your app rapidly for multi cloud deployment.</p>
    <div class="hero-actions">
      <a class="btn btn-outline">Why Nimbrotek?</a>
      <a class="btn btn-accent">Try for <b>free</b></a>
    </div>
  </div>

  <div class="platforms">
    <span class="platform"><span class="mark"></span>Arcvault</span>
    <span class="platform"><span class="mark"></span>Zephyrqa Cloud</span>
    <span class="platform"><span class="mark"></span>Cerulix</span>
    <span class="platform"><span class="mark"></span>Quorvane Cloud</span>
    <span class="platform"><span class="mark"></span>Tessarin Cloud</span>
    <span class="platform"><span class="mark"></span>Halvex</span>
    <span class="platform">
      <svg width="20" height="22" viewBox="0 0 20 22" fill="none" stroke="#fff" stroke-width="1.3" aria-hidden="true"><rect x="2" y="6" width="16" height="15"/><line x1="10" y1="1" x2="10" y2="6"/><rect x="5" y="9" width="3" height="3"/><rect x="12" y="9" width="3" height="3"/><rect x="5" y="15" width="3" height="3"/><rect x="12" y="15" width="3" height="3"/></svg>
      On-premises</span>
  </div>
</header>

<section class="feature">
  <div class="shot">
    <svg width="578" height="407" viewBox="0 0 578 407" aria-hidden="true" stroke="#ececec" stroke-width="1"><line x1="22" y1="27" x2="248" y2="178"/><line x1="552" y1="27" x2="326" y2="178"/><line x1="22" y1="380" x2="262" y2="222"/><line x1="552" y1="380" x2="312" y2="222"/></svg>
    <div class="shot-label">Screenshot of service</div>
  </div>
  <div class="feature-copy">
    <svg width="44" height="38" viewBox="0 0 44 38" fill="none" stroke="#2aa8dc" stroke-width="1.6" aria-hidden="true">
      <path d="M10 30H8a7 7 0 0 1 0-14 11 11 0 0 1 21-5 9 9 0 0 1 7 16"/>
      <circle cx="22" cy="27" r="4"/>
      <path d="M22 19v3M22 32v3M14 27h3M27 27h3M16.5 21.5l2 2M25.5 30.5l2 2M16.5 32.5l2-2M25.5 23.5l2-2"/>
    </svg>
    <h2 class="feature-title">Calculate the cost to migrate clouds</h2>
    <p class="feature-text">USe our free tool to calculate how much your Zephyrqa Run Engine (ZRE) application would cost if you migrated it to one of five different public clouds (including Zephyrqa Compute Engine)</p>
    <a class="btn btn-accent">Try the calculator</a>
  </div>
</section>

<div class="footer-band"></div>
</body>
</html>
```